Construction business card

I need a new business card, they can connect with my logo, brand.
What we do is residential house , design and build
I like: Navy blue / black
I attached our logo, brand,
and, some idea for business card.

```html
<!DOCTYPE html>
<html lang="en">
<head>
<meta charset="utf-8">
<title>Ridgeline Building Group – Business Card</title>
<link href="https://fonts.googleapis.com/css2?family=Arimo:wght@400;700&display=swap" rel="stylesheet">
<style>
  :root {
    --page: #2a2a2c;
    --card: #272729;
    --card-edge: #1f1f21;
    --white: #ffffff;
    --blue: #3a86d0;
    --muted: #d8d8d8;
  }
  * { box-sizing: border-box; margin: 0; padding: 0; }
  html, body {
    width: 1200px; height: 900px; overflow: hidden;
    background: var(--page);
    font-family: "Arimo", Arial, sans-serif;
  }
  .canvas {
    position: relative; width: 1200px; height: 900px;
  }
  .card {
    position: absolute; left: 250px; width: 700px; height: 400px;
    background: var(--card);
    border-radius: 22px;
    box-shadow: 0 10px 30px rgba(0,0,0,.45);
    overflow: hidden;
  }
  .card-front { top: 40px; }
  .card-back { top: 460px; }

  .brand {
    display: flex; align-items: center; gap: 12px;
    color: var(--white); font-weight: 700; text-transform: uppercase;
    letter-spacing: 0.04em;
  }
  .brand-mark { background: var(--blue); flex: none; }
  .card-front .brand {
    position: absolute; left: 50%; top: 50%;
    transform: translate(-50%, -50%);
    font-size: 38px; white-space: nowrap;
  }
  .card-front .brand-mark { width: 26px; height: 26px; }

  .card-back .brand {
    position: absolute; left: 44px; top: 46px;
    font-size: 22px; gap: 9px;
  }
  .card-back .brand-mark { width: 16px; height: 16px; }

  .contact {
    position: absolute; left: 44px; bottom: 44px;
    color: var(--white); font-size: 17px; line-height: 1.35;
  }
  .address { margin-bottom: 16px; }
  .contact-list { list-style: none; }
  .contact-list li { display: flex; align-items: center; gap: 10px; margin-top: 4px; }
  .contact-icon { width: 15px; height: 15px; flex: none; }

  .person {
    position: absolute; right: 70px; top: 150px;
    text-align: right;
  }
  .person-name {
    color: var(--blue); font-weight: 700; font-size: 27px;
    text-transform: uppercase; letter-spacing: 0.01em;
  }
  .person-role { color: var(--white); font-size: 17px; margin-top: 2px; }
  .person-accent {
    position: absolute; right: 40px; top: 138px;
    width: 14px; height: 56px; background: var(--blue);
  }
</style>
</head>
<body>
<main class="canvas">

  <section class="card card-front" aria-label="Card front">
    <div class="brand"><span class="brand-mark"></span>Ridgeline Building Group</div>
  </section>

  <section class="card card-back" aria-label="Card back">
    <div class="brand"><span class="brand-mark"></span>Ridgeline Building Group</div>

    <span class="person-accent"></span>
    <div class="person">
      <p class="person-name">Daniel Hart</p>
      <p class="person-role">CEO/Founder</p>
    </div>

    <div class="contact">
      <p class="address">48 Wattle Grove Rd,<br>Oakvale, VIC 3190</p>
      <ul class="contact-list">
        <li>
          <svg class="contact-icon" viewBox="0 0 24 24" aria-hidden="true"><path fill="#3a86d0" d="M6.6 10.8a15.2 15.2 0 0 0 6.6 6.6l2.2-2.2a1 1 0 0 1 1-.25 11.4 11.4 0 0 0 3.6.57 1 1 0 0 1 1 1V20a1 1 0 0 1-1 1A17 17 0 0 1 3 4a1 1 0 0 1 1-1h3.5a1 1 0 0 1 1 1c0 1.25.2 2.45.57 3.57a1 1 0 0 1-.25 1z"/></svg>
          0400 555 218
        </li>
        <li>
          <svg class="contact-icon" viewBox="0 0 24 24" aria-hidden="true"><rect x="2" y="5" width="20" height="14" rx="2" fill="#3a86d0"/><path d="M3 6l9 7 9-7" stroke="#272729" stroke-width="2" fill="none"/></svg>
          info@ridgelinebuild.com.au
        </li>
        <li>
          <svg class="contact-icon" viewBox="0 0 24 24" aria-hidden="true"><circle cx="12" cy="12" r="10" fill="#3a86d0"/><path d="M2 12h20M12 2c3 3 3 17 0 20M12 2c-3 3-3 17 0 20" stroke="#272729" stroke-width="1.6" fill="none"/></svg>
          ridgelinebuild.com.au
        </li>
      </ul>
    </div>
  </section>

</main>
</body>
</html>
```